STOREFRONT SIGNAGE/ NEW LOGO

Looking for someone to enhance my current sign idea. I own a pawn shop , which is also a gun shop. I want a catchy front sign, which will be a lighted box sign. I may want to incorporate some symbols or character symbology that highlight firearms, such as : guns, ammo, targets, scope retical , gold, diamonds, cash, watches and/or pawn balls, and im open to other ideas, but i do not want it too busy, i want it simple, with a twist. Attached, you will find a very basic design, showing the business name and the verbiage that I would like to be incorporated into the design. God bless and thank you. may the best design win !

```html
<!DOCTYPE html>
<html lang="en">
<head>
<meta charset="utf-8">
<title>Keystone Gold &amp; Gun Exchange – Storefront Sign</title>
<link rel="stylesheet" href="https://fonts.googleapis.com/css2?family=Archivo:wght@800;900&family=Roboto+Condensed:wght@700&display=swap">
<style>
  :root {
    --page-bg: #d9d8dc;
    --gold-light: #e9c566;
    --gold-mid: #d6a93f;
    --gold-deep: #b98a26;
    --label-gold: #c49a1f;
    --ink: #111111;
    --carbon-dark: #0f0f10;
    --carbon-mid: #232325;
    --silver-light: #f2f2f2;
    --silver-dark: #9a9a9a;
    --strip: #ffffff;
  }
  html, body {
    margin: 0;
    padding: 0;
    width: 1181px;
    height: 1200px;
    overflow: hidden;
    background: var(--page-bg);
  }
  .sign-board {
    position: absolute;
    left: 30px;
    top: 460px;
    width: 1121px;
    height: 280px;
    box-shadow: 0 14px 28px rgba(0,0,0,0.35);
  }
  .sign-board svg { display: block; }
  .headline {
    font-family: "Archivo", "Arial Black", sans-serif;
    font-weight: 900;
  }
  .strip-text {
    font-family: "Roboto Condensed", "Arial Narrow", sans-serif;
    font-weight: 700;
    fill: var(--ink);
  }
  .brand-name {
    font-family: "Archivo", "Arial Black", sans-serif;
    font-weight: 900;
    fill: var(--ink);
    letter-spacing: 2px;
  }
</style>
</head>
<body>
  <div class="sign-board">
    <svg width="1121" height="280" viewBox="0 0 1121 280" xmlns="http://www.w3.org/2000/svg">
      <defs>
        <linearGradient id="goldLeaf" x1="0" y1="0" x2="1" y2="1">
          <stop offset="0" stop-color="var(--gold-deep)"/>
          <stop offset="0.35" stop-color="var(--gold-light)"/>
          <stop offset="0.7" stop-color="var(--gold-mid)"/>
          <stop offset="1" stop-color="var(--gold-deep)"/>
        </linearGradient>
        <linearGradient id="carbonField" x1="0" y1="0" x2="1" y2="1">
          <stop offset="0" stop-color="var(--carbon-mid)"/>
          <stop offset="0.5" stop-color="var(--carbon-dark)"/>
          <stop offset="1" stop-color="var(--carbon-mid)"/>
        </linearGradient>
        <linearGradient id="silverType" x1="0" y1="0" x2="1" y2="0">
          <stop offset="0" stop-color="var(--silver-dark)"/>
          <stop offset="0.45" stop-color="var(--silver-light)"/>
          <stop offset="1" stop-color="var(--silver-dark)"/>
        </linearGradient>
      </defs>

      <!-- dark right field -->
      <rect class="gun-field" x="0" y="0" width="1121" height="280" fill="url(#carbonField)" role="img" aria-label="Dark carbon fibre texture"/>

      <!-- gold left field -->
      <polygon class="gold-field" points="0,0 616,0 503,280 0,280" fill="url(#goldLeaf)" role="img" aria-label="Brushed gold leaf texture"/>

      <!-- brand label -->
      <rect class="brand-label" x="412" y="29" width="318" height="56" rx="4" fill="var(--label-gold)" stroke="#3a2d08" stroke-width="2"/>
      <text class="brand-name" x="571" y="70" font-size="38" text-anchor="middle">KEYSTONE</text>

      <!-- ampersand badge -->
      <circle cx="555" cy="144" r="42" fill="#ffffff" stroke="var(--label-gold)" stroke-width="3"/>
      <text class="headline" x="555" y="164" font-size="56" text-anchor="middle" fill="var(--ink)">&amp;</text>

      <!-- gold headline -->
      <text class="headline" x="235" y="122" font-size="86" text-anchor="middle" fill="var(--ink)">Gold</text>
      <text class="headline" x="231" y="196" font-size="86" text-anchor="middle" fill="var(--ink)" textLength="376" lengthAdjust="spacingAndGlyphs">Exchange</text>

      <!-- gun headline -->
      <text class="headline" x="877" y="122" font-size="86" text-anchor="middle" fill="url(#silverType)">Gun</text>
      <text class="headline" x="877" y="196" font-size="86" text-anchor="middle" fill="url(#silverType)" textLength="374" lengthAdjust="spacingAndGlyphs">Exchange</text>

      <!-- left service strip -->
      <polygon class="service-strip" points="0,222 458,222 472,259 0,259" fill="var(--strip)"/>
      <text class="strip-text" x="232" y="247" font-size="17" text-anchor="middle">» PAWN  |  » BUY  |  » SELL  |  » TRADE  |  » LAYAWAY</text>

      <!-- right cash strip -->
      <polygon class="cash-strip" points="649,222 1121,222 1121,259 664,259" fill="var(--strip)"/>
      <text class="strip-text" x="880" y="248" font-size="20" text-anchor="middle">CASH FOR GOLD .......CASH FOR GUNS</text>
    </svg>
  </div>
</body>
</html>
```